TKB Roofing Flyer/Mailer to be used to market to Homeowners

We need to create a flyer than can double as a mailer for our roofing business and possibly be used as a door hanger as well. This flyer will advertise our roofing company in a professional way with pictures as well as clear and precise text about who we are and what we offer. We are open to this flyer being a bi-fold or even a tri-fold. There would need to be an area for address if used as a mailer. A majority of our company information can be found on our website at www.tkbroofing-example.com.

Target Market(s)

Home Owners

Industry/Entity Type

Construction

Colors
0255a3
ffffff

Requirements
Must have
• Professional design, pictures, text with info regarding our company. Website: www.tkbroofing-example.com

```html
<!DOCTYPE html>
<html lang="en">
<head>
<meta charset="utf-8">
<title>TKB Roofing Mailer</title>
<link rel="stylesheet" href="https://fonts.googleapis.com/css2?family=Montserrat:wght@700;800&family=Roboto+Condensed:wght@300;400&family=Roboto:wght@400&display=swap">
<style>
  :root {
    --navy: #1d222b;
    --blue: #0e93d6;
    --brand-blue: #0255a3;
    --white: #ffffff;
    --stage: #eceef1;
    --ink: #23272e;
    --grey-box: #d9d9d9;
    --rule: #555b63;
  }
  * { margin: 0; padding: 0; box-sizing: border-box; }
  html, body { width: 1200px; height: 1200px; overflow: hidden; background: var(--stage); }
  .canvas { position: relative; width: 1200px; height: 1200px; }
  .mailer {
    position: absolute; left: 70px; top: 210px;
    display: flex; width: 1060px; height: 780px;
    box-shadow: 0 14px 40px rgba(0,0,0,.18);
  }
  .panel { position: relative; width: 530px; height: 780px; overflow: hidden; background: var(--white); }
  .panel svg.shapes { position: absolute; inset: 0; }

  /* back (mailing) panel */
  .stamp-box { position: absolute; left: 54px; top: 150px; width: 96px; height: 96px; background: var(--grey-box); }
  .address-lines { position: absolute; left: 190px; top: 80px; display: flex; gap: 44px; }
  .address-lines span { display: block; width: 2px; height: 170px; background: var(--rule); }
  .contact-block {
    position: absolute; left: 36px; top: 540px;
    transform: rotate(-90deg); transform-origin: left top;
    display: flex; align-items: center; gap: 12px;
    font-family: "Roboto Condensed", sans-serif; color: var(--ink);
  }
  .contact-brand { font-family: "Roboto Condensed", sans-serif; font-weight: 400; font-size: 20px; color: var(--brand-blue); white-space: nowrap; }
  .contact-list { list-style: none; font-size: 13px; line-height: 17px; }
  .contact-list li { display: flex; align-items: flex-start; gap: 6px; white-space: nowrap; }
  .contact-list svg { width: 10px; height: 10px; margin-top: 3px; flex: none; }

  /* cover panel */
  .cover-brand {
    position: absolute; left: 0; right: 40px; top: 70px; text-align: center;
    font-family: "Roboto Condensed", sans-serif; color: var(--white);
  }
  .cover-brand .name { font-size: 46px; font-weight: 400; letter-spacing: 2px; }
  .cover-brand .tagline { font-size: 13px; font-weight: 300; letter-spacing: 1px; }
  .headline { position: absolute; left: 50px; top: 420px; line-height: 1; }
  .headline .light { display: block; font-family: "Roboto Condensed", sans-serif; font-weight: 300; font-size: 60px; color: var(--ink); }
  .headline .bold { display: block; font-family: "Montserrat", sans-serif; font-weight: 800; font-size: 46px; color: var(--white); line-height: 1.02; }
  .url-bar {
    position: absolute; left: 150px; right: 0; top: 670px; height: 52px;
    background: var(--white); display: flex; align-items: center; padding-left: 30px;
    font-family: "Roboto", sans-serif; font-size: 19px; letter-spacing: 3px; color: var(--ink);
  }
</style>
</head>
<body>
<div class="canvas">
  <div class="mailer">

    <section class="panel panel-back">
      <svg class="shapes" viewBox="0 0 530 780" width="530" height="780">
        <defs>
          <linearGradient id="house-tones" x1="0" y1="0" x2="0" y2="1">
            <stop offset="0" stop-color="#2b3440"/>
            <stop offset=".35" stop-color="#7a8a8c"/>
            <stop offset=".6" stop-color="#9a5a4a"/>
            <stop offset="1" stop-color="#4f6d32"/>
          </linearGradient>
        </defs>
        <polygon points="530,70 530,110 40,780 0,780" fill="#1d222b"/>
        <polygon points="530,110 530,120 48,780 40,780" fill="#ffffff"/>
        <polygon points="530,120 530,780 48,780" fill="url(#house-tones)" role="img" aria-label="Photo of a red brick two-storey family home with a dark shingle roof"/>
      </svg>
      <div class="address-lines"><span></span><span></span><span></span><span></span></div>
      <div class="stamp-box"></div>
      <div class="contact-block">
        <div class="contact-brand">TKB Roofing</div>
        <ul class="contact-list">
          <li><svg viewBox="0 0 12 12"><path d="M2 1l2 0 1 3-1.5 1a6 6 0 0 0 3.5 3.5L8 7l3 1v2a1 1 0 0 1-1 1A9 9 0 0 1 1 2a1 1 0 0 1 1-1z" fill="#23272e"/></svg>555-010-4827</li>
          <li><svg viewBox="0 0 12 12"><path d="M6 0a4 4 0 0 1 4 4c0 3-4 8-4 8S2 7 2 4a4 4 0 0 1 4-4z" fill="#23272e"/><circle cx="6" cy="4" r="1.5" fill="#fff"/></svg>1200 Maple Crest Drive<br>Fishers, IN 46000</li>
          <li><svg viewBox="0 0 12 12"><circle cx="6" cy="6" r="5" fill="#23272e"/></svg>info@tkbroofing-example.com</li>
          <li><svg viewBox="0 0 12 12"><circle cx="6" cy="6" r="5" fill="#23272e"/></svg>www.tkbroofing-example.com</li>
        </ul>
      </div>
    </section>

    <section class="panel panel-cover">
      <svg class="shapes" viewBox="0 0 530 780" width="530" height="780">
        <defs>
          <linearGradient id="field-tones" x1="0" y1="0" x2="0" y2="1">
            <stop offset="0" stop-color="#3d6fc2"/>
            <stop offset=".45" stop-color="#b9c6cf"/>
            <stop offset=".62" stop-color="#d9a77e"/>
            <stop offset=".8" stop-color="#4f9a2c"/>
            <stop offset="1" stop-color="#2f7a1c"/>
          </linearGradient>
          <linearGradient id="blue-shade" x1="0" y1="0" x2="1" y2="1">
            <stop offset="0" stop-color="#0e93d6"/>
            <stop offset="1" stop-color="#0a7fc0"/>
          </linearGradient>
        </defs>
        <polygon points="0,0 480,0 260,411 0,210" fill="#1d222b"/>
        <polygon points="480,0 530,0 530,620 260,411" fill="url(#field-tones)" role="img" aria-label="Photo of an open hand holding a small model house over green grass under a blue sky"/>
        <polygon points="0,210 530,620 530,780 50,780" fill="url(#blue-shade)"/>
      </svg>
      <div class="cover-brand">
        <div class="name">TKB Roofing</div>
        <div class="tagline">Trusted Keystone Builders</div>
      </div>
      <h1 class="headline">
        <span class="light">INDY'S</span>
        <span class="bold">PREMIER</span>
        <span class="bold">ROOFING</span>
        <span class="light">CONTRACTOR</span>
      </h1>
      <div class="url-bar">www.tkbroofing-example.com</div>
    </section>

  </div>
</div>
</body>
</html>
```